2021 IT Training Presentation Deck Refresh

Copper Lantern is an IT education services firm. We teach IT industry standards and technologies. We are in need of an updated training presentation deck that factors in a fresh take for:

1) Agenda/Table of Contents
2) Chapter Topic Summary
2) Chapter Introduction and Learning Objectives
3) Chapter Recaps
4) Important Point/Pro Tip emphasis
5) Warning Message
6) Mini Quiz layout
7) Lab Exercise Introduction
7) Deck Close Out

Incorporating the official Copper Lantern colour palette for materials that will likely be used in self-paced/online recorded versions of courses.

Target Market(s)

IT

Industry/Entity Type

Computer Training

Requirements
Nice to have
• placeholder sections for images of IT workers in an office or by a computer

```html
<!DOCTYPE html>
<html lang="en">
<head>
<meta charset="utf-8">
<title>Copper Lantern – Presentation Template</title>
<link href="https://fonts.googleapis.com/css2?family=Barlow+Semi+Condensed:wght@400&family=Roboto:wght@300;400;500;700&display=swap" rel="stylesheet">
<style>
  :root {
    --navy: #2a2d6c;
    --navy-deep: #23265c;
    --royal: #2f3f91;
    --blue: #4a78c2;
    --sky: #5b8fd8;
    --pale: #a5cbf6;
    --ink: #1f2340;
    --body: #3b3f5c;
    --rule: #c9cfe0;
    --white: #ffffff;
    --paper: #ffffff;
  }
  * { box-sizing: border-box; margin: 0; padding: 0; }
  html, body { width: 1200px; height: 2194px; overflow: hidden; background: var(--paper); }
  body { position: relative; font-family: "Roboto", Arial, sans-serif; color: var(--body); }

  /* Header */
  .brand { position: absolute; left: 93px; top: 60px; width: 280px; height: 130px; }
  .brand-dot { position: absolute; left: 0; top: 0; width: 60px; height: 60px; border-radius: 50%; background: var(--royal); }
  .brand-name { position: absolute; left: 0; top: 82px; font-family: "Barlow Semi Condensed", sans-serif; font-weight: 400; font-size: 40px; line-height: 1; color: var(--blue); letter-spacing: 1px; white-space: nowrap; }
  .sheet-title { position: absolute; left: 424px; top: 80px; font-family: "Barlow Semi Condensed", sans-serif; font-weight: 400; font-size: 58px; line-height: 1.1; letter-spacing: 2px; color: var(--navy-deep); white-space: nowrap; }
  .sheet-title .accent { color: var(--blue); }

  /* Slide frame */
  .slide { position: absolute; width: 444px; height: 249px; overflow: hidden; background: var(--white); box-shadow: 0 6px 16px rgba(20, 25, 60, .28); }
  .slide-title { position: absolute; left: 26px; top: 13px; font-size: 17px; font-weight: 400; color: var(--ink); white-space: nowrap; }
  .rule { position: absolute; left: 26px; top: 38px; width: 380px; height: 0.6px; background: var(--rule); }
  .mark { position: absolute; right: 16px; top: 17px; font-size: 6px; font-weight: 500; color: var(--blue); }
  .foot-url { position: absolute; left: 24px; bottom: 8px; font-size: 4.2px; color: var(--blue); }
  .foot-num { position: absolute; right: 24px; bottom: 8px; font-size: 4.2px; color: var(--blue); }
  .fine { font-size: 4.4px; line-height: 1.6; text-align: justify; color: var(--body); }
  .photo { position: absolute; }

  /* 1 cover */
  .cover { background: var(--navy); }
  .cover .photo { left: 0; top: 34px; width: 444px; height: 180px; background: linear-gradient(100deg, #4c5274 0%, #6b7090 40%, #3c4166 75%, #2d3157 100%); }
  .cover-title { position: absolute; left: 0; right: 0; top: 94px; text-align: center; color: var(--white); font-weight: 300; font-size: 15px; line-height: 1.25; }
  .cover-sub { position: absolute; left: 0; right: 0; top: 140px; text-align: center; color: #e3e6f2; font-weight: 300; font-size: 9px; line-height: 1.4; }
  .cover .foot-url, .cover .foot-num { color: #b9c4ea; }

  /* 2 cover alt */
  .cover-alt .photo { inset: 0; background: linear-gradient(135deg, #b7d3dc 0%, #96bac8 55%, #7ea4b4 100%); }
  .cover-alt .alt-brand { position: absolute; left: 0; right: 0; top: 70px; display: flex; justify-content: center; align-items: center; gap: 10px; }
  .cover-alt .alt-brand .alt-dot { width: 40px; height: 40px; border-radius: 50%; background: var(--royal); }
  .cover-alt .alt-brand span.alt-name { font-size: 28px; font-weight: 500; color: var(--royal); }
  .cover-alt .alt-title { position: absolute; left: 0; right: 0; top: 186px; text-align: center; font-size: 13.5px; font-weight: 500; color: var(--navy-deep); }
  .cover-alt .alt-sub { position: absolute; left: 0; right: 0; top: 205px; text-align: center; font-size: 7px; font-weight: 300; color: var(--white); }
  .cover-alt .foot-num { color: #eef; }

  /* 3 agenda */
  .agenda .photo { left: 0; top: 0; width: 163px; height: 249px; background: linear-gradient(180deg, #6d6a73 0%, #5a4b46 55%, #7b5538 100%); }
  .agenda .num-band { position: absolute; left: 98px; top: 0; width: 65px; height: 249px; background: rgba(42, 45, 108, .78); }
  .agenda .nums { position: absolute; left: 125px; top: 64px; list-style: none; color: var(--white); font-size: 7px; font-weight: 500; }
  .agenda .nums li { height: 17.2px; }
  .agenda .slide-title { left: 174px; }
  .agenda .rule { left: 174px; width: 250px; }
  .agenda .items { position: absolute; left: 203px; top: 58px; width: 171px; list-style: none; }
  .agenda .items li { height: 17.2px; padding-top: 5px; border-top: 0.6px solid var(--rule); font-size: 6.4px; font-weight: 500; color: var(--navy-deep); }
  .agenda .items li:last-child { border-bottom: 0.6px solid var(--rule); }

  /* 4 & 5 summaries */
  .summary ol { position: absolute; left: 26px; top: 58px; padding-left: 9px; }
  .summary ol li { margin-bottom: 4px; font-size: 4.4px; line-height: 1.6; text-align: justify; }
  .summary-one ol { width: 386px; }
  .summary-two .col { position: absolute; top: 58px; width: 190px; }
  .summary-two .col ol { position: static; }
  .summary-two .col-a { left: 26px; }
  .summary-two .col-b { left: 232px; }
  .summary-two .lead { font-size: 4.4px; line-height: 1.6; text-align: justify; margin-bottom: 4px; padding-left: 9px; }

  /* 6 objectives */
  .objectives .intro { position: absolute; left: 26px; top: 46px; width: 386px; }
  .objectives .band { position: absolute; left: 0; top: 109px; width: 444px; height: 140px; background: linear-gradient(90deg, rgba(42,45,108,.96) 0%, rgba(47,63,145,.85) 60%, rgba(42,45,108,.95) 100%), linear-gradient(180deg, #6a74a8, #2a2d6c); }
  .objectives .obj { position: absolute; top: 89px; width: 92px; }
  .objectives .obj-icon { width: 42px; height: 42px; margin-left: 25px; border-radius: 50%; background: var(--royal); border: 1px solid rgba(255,255,255,.25); display: flex; align-items: center; justify-content: center; }
  .objectives .obj h4 { margin-top: 24px; font-size: 5.5px; font-weight: 700; color: var(--white); }
  .objectives .obj p { margin-top: 4px; font-size: 3.9px; line-height: 1.55; color: #dfe3f5; text-align: justify; }

  /* 7 recaps */
  .recaps .lead { position: absolute; left: 27px; top: 52px; width: 118px; }
  .recaps ul { position: absolute; left: 27px; top: 142px; width: 118px; padding-left: 7px; font-size: 4.4px; line-height: 2.25; color: var(--body); }
  .recaps .step { position: absolute; width: 120px; }
  .recaps .step .disc { position: absolute; left: 0; top: 0; width: 34px; height: 34px; border-radius: 50%; color: var(--white); font-size: 12px; display: flex; align-items: center; justify-content: center; }
  .recaps .step h5 { position: absolute; left: 45px; top: 2px; font-size: 4.4px; font-weight: 700; color: var(--ink); }
  .recaps .step p { position: absolute; left: 45px; top: 10px; width: 78px; font-size: 3.4px; line-height: 1.5; color: var(--body); }

  /* 8 checklist */
  .checklist .intro { position: absolute; left: 26px; top: 46px; width: 390px; }
  .checklist .check-col { position: absolute; top: 76px; list-style: none; }
  .checklist .check-col li { height: 25.4px; display: flex; align-items: center; gap: 8px; font-size: 4.8px; color: var(--blue); }
  .checklist .check-col svg { width: 16px; height: 16px; flex: none; }

  /* 9 pro tip */
  .protip .water { position: absolute; left: 277px; top: 0; width: 167px; height: 249px; background: linear-gradient(180deg, #a9cff8 0%, #9ac3f0 22%, #5d8fc8 30%, #3f72ad 70%, #6894c6 100%); }
  .protip .rule { width: 250px; }
  .protip .tip { position: absolute; left: 33px; width: 176px; text-align: right; }
  .protip .tip h5 { font-size: 6px; font-weight: 700; color: var(--ink); margin-bottom: 4px; }
  .protip .tip p { font-size: 3.5px; line-height: 1.6; text-align: justify; }
  .protip .thumb { left: 224px; width: 114px; height: 48px; }

  /* 10 break */
  .break .photo { inset: 0; background: linear-gradient(135deg, #9dbad6 0%, #7fa0c8 40%, #5878ad 70%, #8eaed2 100%); }
  .break .break-title { position: absolute; left: 57px; top: 88px; font-size: 28px; font-weight: 500; line-height: 1.1; color: #dce8f8; }
  .break .break-title span:first-child { color: var(--navy-deep); }

  /* 11 emphasis */
  .emphasis .band { position: absolute; left: 0; top: 0; width: 444px; height: 119px; background: linear-gradient(90deg, #2f4f99 0%, #3d5ea6 45%, #2f4686 100%); }
  .emphasis .slide-title { color: var(--white); }
  .emphasis .rule { background: rgba(255,255,255,.4); }
  .emphasis .band-text { position: absolute; left: 26px; top: 62px; width: 390px; font-size: 6.4px; line-height: 1.35; color: var(--white); }
  .emphasis .pt { position: absolute; top: 134px; width: 78px; text-align: center; }
  .emphasis .pt .disc { width: 26px; height: 26px; margin: 0 auto; border-radius: 50%; color: var(--white); font-size: 9px; display: flex; align-items: center; justify-content: center; }
  .emphasis .pt h5 { margin-top: 9px; font-size: 4.6px; font-weight: 500; color: var(--royal); }
  .emphasis .pt p { margin-top: 4px; font-size: 4.5px; line-height: 1.45; text-align: justify; color: var(--royal); }

  /* 12 lab */
  .lab .intro { position: absolute; left: 22px; top: 46px; width: 250px; font-size: 5.2px; line-height: 1.3; text-align: justify; color: var(--ink); }
  .lab .item { position: absolute; left: 56px; width: 170px; }
  .lab .item .disc { position: absolute; left: 0; top: 0; width: 29px; height: 29px; border-radius: 50%; color: var(--white); font-size: 8px; display: flex; align-items: center; justify-content: center; }
  .lab .item h5 { position: absolute; left: 42px; top: 0; font-size: 4.4px; font-weight: 500; color: var(--blue); white-space: nowrap; }
  .lab .item p { position: absolute; left: 42px; top: 10px; width: 128px; font-size: 4.4px; line-height: 1.5; color: var(--royal); text-align: justify; }
  .lab .photo { left: 284px; top: 42px; width: 132px; height: 180px; background: linear-gradient(180deg, #8a8b86 0%, #4d4640 50%, #6a4a30 100%); }

  /* 13 quiz */
  .quiz { background: var(--navy); }
  .quiz h3 { position: absolute; left: 0; right: 0; top: 20px; text-align: center; font-size: 19px; font-weight: 300; color: #8fb8f0; }
  .quiz .quiz-sub { position: absolute; left: 0; right: 0; top: 52px; text-align: center; font-size: 6px; color: #6f8fd6; }
  .quiz .q { position: absolute; width: 125px; }
  .quiz .q .qn { position: absolute; left: 0; top: 12px; font-size: 8px; color: var(--white); }
  .quiz .q .ql { position: absolute; left: 17px; top: 0; font-size: 4.6px; color: var(--sky); }
  .quiz .q p { position: absolute; left: 17px; top: 9px; width: 108px; font-size: 5px; line-height: 1.45; color: var(--white); }
  .quiz .foot-url { color: #a8bbea; }

  /* 14 important point */
  .point .copy { position: absolute; left: 25px; top: 48px; width: 118px; font-size: 4.6px; line-height: 1.5; text-align: justify; color: var(--ink); }
  .point .photo { left: 157px; top: 45px; width: 262px; height: 177px; background: linear-gradient(170deg, #7a7f83 0%, #4b4a48 45%, #5e4530 100%); }
</style>
</head>
<body>

<header>
  <div class="brand"><span class="brand-dot"></span><span class="brand-name">COPPER LANTERN</span></div>
  <h1 class="sheet-title">POWERPOINT <span class="accent">TEMPLATE</span></h1>
</header>

<!-- Row 1 -->
<section class="slide cover" style="left:93px; top:251px;">
  <div class="photo" role="img" aria-label="Photo of IT professionals working at computer screens"></div>
  <h2 class="cover-title">COPPER LANTERN IT<br>EDUCATION SERVICES</h2>
  <p class="cover-sub">WE TEACH IT INDUSTRY STANDARDS<br>AND TECHNOLOGIES.</p>
  <span class="foot-url">www.copper-lantern.com</span><span class="foot-num">1</span>
</section>

<section class="slide cover-alt" style="left:659px; top:251px;">
  <div class="photo" role="img" aria-label="Photo of a classroom with learners at laptops, tinted pale teal"></div>
  <div class="alt-brand"><span class="alt-dot"></span><span class="alt-name">Copper Lantern</span></div>
  <h2 class="alt-title">COPPER LANTERN IT EDUCATION SERVICES</h2>
  <p class="alt-sub">WE TEACH IT INDUSTRY STANDARDS AND TECHNOLOGIES.</p>
  <span class="foot-num">2</span>
</section>

<!-- Row 2 -->
<section class="slide agenda" style="left:93px; top:524px;">
  <div class="photo" role="img" aria-label="Photo of an IT worker with headphones at a laptop, seen from above"></div>
  <div class="num-band"></div>
  <ol class="nums"><li>01</li><li>02</li><li>03</li><li>04</li><li>05</li><li>06</li><li>07</li><li>08</li></ol>
  <h3 class="slide-title">Agenda</h3><div class="rule"></div>
  <span class="mark">Copper Lantern</span>
  <ul class="items">
    <li>Chapter Topic Summary</li>
    <li>Chapter Introduction and Learning Objectives</li>
    <li>Chapter Recaps</li>
    <li>Important Point/Pro Tip emphasis</li>
    <li>Warning Message</li>
    <li>Mini Quiz layout</li>
    <li>Lab Exercise Introduction</li>
    <li>Deck Close Out</li>
  </ul>
  <span class="foot-num">3</span>
</section>

<section class="slide summary summary-one" style="left:659px; top:524px;">
  <h3 class="slide-title">Topic summary one column</h3><div class="rule"></div>
  <span class="mark">Copper Lantern</span>
  <ol>
    <li>Learners review the core standard, why it matters and how teams apply it in daily work. Each step is shown with a short example, a checklist and a note on common mistakes to avoid. Use this space to summarise the key idea before moving on to the next lesson. Learners review the core standard, why it matters and how teams apply it in daily work.</li>
    <li>Learners review the core standard, why it matters and how teams apply it in daily work. Each step is shown with a short example, a checklist and a note on common mistakes to avoid. Use this space to summarise the key idea before moving on to the next lesson. Learners review the core standard, why it matters and how teams apply it in daily work.</li>
    <li>Learners review the core standard, why it matters and how teams apply it in daily work. Each step is shown with a short example, a checklist and a note on common mistakes to avoid. Use this space to summarise the key idea before moving on to the next lesson. Learners review the core standard, why it matters and how teams apply it in daily work.</li>
    <li>Learners review the core standard, why it matters and how teams apply it in daily work. Each step is shown with a short example, a checklist and a note on common mistakes to avoid. Use this space to summarise the key idea before moving on to the next lesson. Learners review the core standard, why it matters and how teams apply it in daily work.</li>
  </ol>
  <span class="foot-url">www.copper-lantern.com</span><span class="foot-num">4</span>
</section>

<!-- Row 3 -->
<section class="slide summary summary-two" style="left:93px; top:795px;">
  <h3 class="slide-title">Topic summary two column</h3><div class="rule"></div>
  <span class="mark">Copper Lantern</span>
  <div class="col col-a">
    <ol>
      <li>Learners review the core standard, why it matters and how teams apply it in daily work. Each step is shown with a short example, a checklist and a note on common mistakes to avoid. Use this space to summarise the key idea before moving on to the next lesson.</li>
      <li>Each step is shown with a short example, a checklist and a note on common mistakes to avoid. Learners review the core standard, why it matters and how teams apply it in daily work.</li>
      <li>Use this space to summarise the key idea before moving on to the next lesson. Learners review the core standard, why it matters and how teams apply it in daily work. Each step is shown with a short example, a checklist and a note on common mistakes to avoid.</li>
      <li>Learners review the core standard, why it matters and how teams apply it in daily work.</li>
    </ol>
  </div>
  <div class="col col-b">
    <p class="lead">Use this space to summarise the key idea before moving on to the next lesson.</p>
    <ol start="5">
      <li>Learners review the core standard, why it matters and how teams apply it in daily work. Each step is shown with a short example, a checklist and a note on common mistakes to avoid. Use this space to summarise the key idea before moving on to the next lesson.</li>
      <li>Each step is shown with a short example, a checklist and a note on common mistakes to avoid. Use this space to summarise the key idea before moving on to the next lesson. Learners review the core standard, why it matters and how teams apply it in daily work.</li>
    </ol>
  </div>
  <span class="foot-url">www.copper-lantern.com</span><span class="foot-num">5</span>
</section>

<section class="slide objectives" style="left:659px; top:795px;">
  <h3 class="slide-title">Introduction and Learning Objectives</h3><div class="rule"></div>
  <span class="mark">Copper Lantern</span>
  <p class="intro fine">Learners review the core standard, why it matters and how teams apply it in daily work. Each step is shown with a short example, a checklist and a note on common mistakes to avoid.</p>
  <div class="band" role="img" aria-label="Photo of an office training room under a navy overlay"></div>
  <div class="obj" style="left:19px;">
    <div class="obj-icon"><svg width="20" height="20" viewBox="0 0 20 20" fill="none" stroke="#fff" stroke-width="1.4"><circle cx="8.5" cy="8.5" r="6"/><path d="M13 13l5 5M4.5 9h2l1-2.5 2 5 1-2.5h2"/></svg></div>
    <h4>Learning objective</h4>
    <p>Learners review the core standard, why it matters and how teams apply it in daily work. Each step is shown with a short example, a checklist and a note on common mistakes to avoid.</p>
  </div>
  <div class="obj" style="left:125px;">
    <div class="obj-icon"><svg width="20" height="20" viewBox="0 0 20 20" fill="none" stroke="#fff" stroke-width="1.4"><path d="M5 18v-4a6 6 0 1 1 9-5l1.5 3h-2v3h-3v3"/><circle cx="9.5" cy="8" r="2"/></svg></div>
    <h4>Learning objective</h4>
    <p>Learners review the core standard, why it matters and how teams apply it in daily work. Each step is shown with a short example, a checklist and a note on common mistakes to avoid.</p>
  </div>
  <div class="obj" style="left:231px;">
    <div class="obj-icon"><svg width="20" height="20" viewBox="0 0 20 20" fill="none" stroke="#fff" stroke-width="1.4"><rect x="3" y="3" width="14" height="10"/><path d="M10 13v4M6 18l4-1 4 1M6 10l3-3 2 2 3-3"/></svg></div>
    <h4>Learning objective</h4>
    <p>Learners review the core standard, why it matters and how teams apply it in daily work. Each step is shown with a short example, a checklist and a note on common mistakes to avoid.</p>
  </div>
  <div class="obj" style="left:337px;">
    <div class="obj-icon"><svg width="20" height="20" viewBox="0 0 20 20" fill="none" stroke="#fff" stroke-width="1.4"><circle cx="10" cy="10" r="7"/><circle cx="10" cy="10" r="3.5"/><path d="M10 10l7-7M14 3h3v3"/></svg></div>
    <h4>Learning objective</h4>
    <p>Learners review the core standard, why it matters and how teams apply it in daily work. Each step is shown with a short example, a checklist and a note on common mistakes to avoid.</p>
  </div>
</section>

<!-- Row 4 -->
<section class="slide recaps" style="left:93px; top:1068px;">
  <h3 class="slide-title">Chapter recaps</h3><div class="rule"></div>
  <span class="mark">Copper Lantern</span>
  <p class="lead fine">Learners review the core standard, why it matters and how teams apply it in daily work. Each step is shown with a short example, a checklist and a note on common mistakes to avoid. Use this space to summarise the key idea before moving on to the next lesson. Learners review the core standard, why it matters and how teams apply it in daily work.</p>
  <ul>
    <li>Review the core standard</li>
    <li>Check tools used by teams</li>
    <li>Note common mistakes</li>
    <li>Apply steps in daily work</li>
    <li>Summarise the key idea</li>
    <li>Practise with a short task</li>
    <li>Move to the next lesson</li>
  </ul>
  <div class="step" style="left:167px; top:56px;"><span class="disc" style="background:var(--navy);">1</span><h5>KEY POINT</h5><p>Learners review the core standard, why it matters and how teams apply it in daily work.</p></div>
  <div class="step" style="left:296px; top:56px;"><span class="disc" style="background:var(--royal);">2</span><h5>KEY POINT</h5><p>Learners review the core standard, why it matters and how teams apply it in daily work.</p></div>
  <div class="step" style="left:167px; top:115px;"><span class="disc" style="background:#4d64a3;">3</span><h5>KEY POINT</h5><p>Learners review the core standard, why it matters and how teams apply it in daily work.</p></div>
  <div class="step" style="left:296px; top:115px;"><span class="disc" style="background:#6b8fd1;">4</span><h5>KEY POINT</h5><p>Learners review the core standard, why it matters and how teams apply it in daily work.</p></div>
  <div class="step" style="left:167px; top:174px;"><span class="disc" style="background:#4a9ee2;">5</span><h5>KEY POINT</h5><p>Learners review the core standard, why it matters and how teams apply it in daily work.</p></div>
  <div class="step" style="left:296px; top:174px;"><span class="disc" style="background:#2f4790;">6</span><h5>KEY POINT</h5><p>Learners review the core standard, why it matters and how teams apply it in daily work.</p></div>
  <span class="foot-url">www.copper-lantern.com</span><span class="foot-num">7</span>
</section>

<section class="slide checklist" style="left:659px; top:1068px;">
  <h3 class="slide-title">Important Point/Pro Tip emphasis</h3><div class="rule"></div>
  <span class="mark">Copper Lantern</span>
  <p class="intro fine">Learners review the core standard, why it matters and how teams apply it in daily work. Each step is shown with a short example, a checklist and a note on common mistakes to avoid.</p>
  <ul class="check-col" style="left:34px;">
    <li><svg viewBox="0 0 16 16"><circle cx="8" cy="8" r="7.2" fill="none" stroke="#2a2d6c"/><path d="M5.5 5.5l5 5M10.5 5.5l-5 5" stroke="#2a2d6c" stroke-width="1"/></svg>There are many variations of passages of lorem ipsum .</li>
    <li><svg viewBox="0 0 16 16"><circle cx="8" cy="8" r="7.2" fill="none" stroke="#2a2d6c"/><path d="M5 8.3l2 2 4-4.5" fill="none" stroke="#2a2d6c" stroke-width="1"/></svg>There are many variations of passages of lorem ipsum .</li>
    <li><svg viewBox="0 0 16 16"><circle cx="8" cy="8" r="7.2" fill="none" stroke="#2a2d6c"/><path d="M5.5 5.5l5 5M10.5 5.5l-5 5" stroke="#2a2d6c" stroke-width="1"/></svg>There are many variations of passages of lorem ipsum .</li>
    <li><svg viewBox="0 0 16 16"><circle cx="8" cy="8" r="7.2" fill="none" stroke="#2a2d6c"/><path d="M5.5 5.5l5 5M10.5 5.5l-5 5" stroke="#2a2d6c" stroke-width="1"/></svg>There are many variations of passages of lorem ipsum .</li>
    <li><svg viewBox="0 0 16 16"><circle cx="8" cy="8" r="7.2" fill="none" stroke="#2a2d6c"/><path d="M5 8.3l2 2 4-4.5" fill="none" stroke="#2a2d6c" stroke-width="1"/></svg>There are many variations of passages of lorem ipsum .</li>
    <li><svg viewBox="0 0 16 16"><circle cx="8" cy="8" r="7.2" fill="none" stroke="#2a2d6c"/><path d="M5.5 5.5l5 5M10.5 5.5l-5 5" stroke="#2a2d6c" stroke-width="1"/></svg>There are many variations of passages of lorem ipsum .</li>
  </ul>
  <ul class="check-col" style="left:228px;">
    <li><svg viewBox="0 0 16 16"><circle cx="8" cy="8" r="7.2" fill="none" stroke="#2a2d6c"/><path d="M5.5 5.5l5 5M10.5 5.5l-5 5" stroke="#2a2d6c" stroke-width="1"/></svg>There are many variations of passages of lorem ipsum .</li>
    <li><svg viewBox="0 0 16 16"><circle cx="8" cy="8" r="7.2" fill="none" stroke="#2a2d6c"/><path d="M5 8.3l2 2 4-4.5" fill="none" stroke="#2a2d6c" stroke-width="1"/></svg>There are many variations of passages of lorem ipsum .</li>
    <li><svg viewBox="0 0 16 16"><circle cx="8" cy="8" r="7.2" fill="none" stroke="#2a2d6c"/><path d="M5.5 5.5l5 5M10.5 5.5l-5 5" stroke="#2a2d6c" stroke-width="1"/></svg>There are many variations of passages of lorem ipsum .</li>
    <li><svg viewBox="0 0 16 16"><circle cx="8" cy="8" r="7.2" fill="none" stroke="#2a2d6c"/><path d="M5.5 5.5l5 5M10.5 5.5l-5 5" stroke="#2a2d6c" stroke-width="1"/></svg>There are many variations of passages of lorem ipsum .</li>
    <li><svg viewBox="0 0 16 16"><circle cx="8" cy="8" r="7.2" fill="none" stroke="#2a2d6c"/><path d="M5 8.3l2 2 4-4.5" fill="none" stroke="#2a2d6c" stroke-width="1"/></svg>There are many variations of passages of lorem ipsum .</li>
    <li><svg viewBox="0 0 16 16"><circle cx="8" cy="8" r="7.2" fill="none" stroke="#2a2d6c"/><path d="M5.5 5.5l5 5M10.5 5.5l-5 5" stroke="#2a2d6c" stroke-width="1"/></svg>There are many variations of passages of lorem ipsum .</li>
  </ul>
  <span class="foot-url">www.copper-lantern.com</span><span class="foot-num">8</span>
</section>

<!-- Row 5 -->
<section class="slide protip" style="left:93px; top:1340px;">
  <div class="water" role="img" aria-label="Photo of open sea water under a pale blue sky"></div>
  <h3 class="slide-title">Pro Tip emphasis</h3><div class="rule"></div>
  <span class="mark">Copper Lantern</span>
  <div class="tip" style="top:68px;"><h5>Subtitle Example here</h5><p>Learners review the core standard, why it matters and how teams apply it in daily work. Each step is shown with a short example, a checklist and a note on common mistakes to avoid. Use this space to summarise the key idea before moving on to the next lesson.</p></div>
  <div class="tip" style="top:126px;"><h5>Subtitle Example here</h5><p>Learners review the core standard, why it matters and how teams apply it in daily work. Each step is shown with a short example, a checklist and a note on common mistakes to avoid. Use this space to summarise the key idea before moving on to the next lesson.</p></div>
  <div class="tip" style="top:184px;"><h5>Subtitle Example here</h5><p>Learners review the core standard, why it matters and how teams apply it in daily work. Each step is shown with a short example, a checklist and a note on common mistakes to avoid. Use this space to summarise the key idea before moving on to the next lesson.</p></div>
  <div class="photo thumb" style="top:64px; background:linear-gradient(120deg,#5b6070,#9aa0aa 60%,#6a6f7c);" role="img" aria-label="Photo of an IT worker with headphones at a laptop"></div>
  <div class="photo thumb" style="top:122px; background:linear-gradient(120deg,#4a3f36,#7b6a58 55%,#3e3a38);" role="img" aria-label="Photo of a group of learners at a training table"></div>
  <div class="photo thumb" style="top:179px; background:linear-gradient(120deg,#c9ccd0,#8f959e 55%,#5c6470);" role="img" aria-label="Photo of colleagues working at computer monitors"></div>
  <span class="foot-url">www.copper-lantern.com</span>
</section>

<section class="slide break" style="left:659px; top:1340px;">
  <div class="photo" role="img" aria-label="Photo of a training room with pendant lamps, tinted blue"></div>
  <h2 class="break-title"><span>Break</span><br><span>Section</span><br><span>Slide</span></h2>
</section>

<!-- Row 6 -->
<section class="slide emphasis" style="left:93px; top:1613px;">
  <div class="band" role="img" aria-label="Photo of an office with people at desks under a blue overlay"></div>
  <h3 class="slide-title">Important Point/Pro Tip emphasis</h3><div class="rule"></div>
  <span class="mark" style="color:#fff;">Copper Lantern</span>
  <p class="band-text">Lorem esomzdo ipsos doloramet, deramset. Fosduom dolores etomda jam takimta sanctus esto ipsusit drin for the the murda insam ons indoa nurds iodsa the hrunds nursna druamet.Sanctus est Lorem sus ipsusitn theo druamet. Lorem esomzdo ipsos doloramet, deramset Das forem sus ast vero ob eosm etprsa accusam eturdn ao justo fosduno dolores etomda the jamo teclita kuasd fruda fr gubergren.</p>
  <div class="pt" style="left:48px;"><span class="disc" style="background:var(--navy);">1</span><h5>SUBITLE EXAMPLE HERE</h5><p>Lorem ipsum dolor sit amet, consectetur adipiscing elit. Fusce diam tortor, mattis quis dapibus vitae, euismod non.</p></div>
  <div class="pt" style="left:138px;"><span class="disc" style="background:var(--royal);">2</span><h5>SUBITLE EXAMPLE HERE</h5><p>Lorem ipsum dolor sit amet, consectetur adipiscing elit. Fusce diam tortor, mattis quis dapibus vitae, euismod non.</p></div>
  <div class="pt" style="left:228px;"><span class="disc" style="background:#3a62ad;">3</span><h5>SUBITLE EXAMPLE HERE</h5><p>Lorem ipsum dolor sit amet, consectetur adipiscing elit. Fusce diam tortor, mattis quis dapibus vitae, euismod non.</p></div>
  <div class="pt" style="left:320px;"><span class="disc" style="background:var(--sky);">4</span><h5 style="color:var(--sky);">SUBITLE EXAMPLE HERE</h5><p style="color:var(--sky);">Lorem ipsum dolor sit amet, consectetur adipiscing elit. Fusce diam tortor, mattis quis dapibus vitae, euismod non.</p></div>
  <span class="foot-url">www.copper-lantern.com</span><span class="foot-num">12</span>
</section>

<section class="slide lab" style="left:659px; top:1613px;">
  <h3 class="slide-title">Lab&nbsp; Exercise Introduction</h3><div class="rule"></div>
  <span class="mark">Copper Lantern</span>
  <p class="intro">Lorem esomzdo ipsos doloramet, deramset. Fosduom dolores etomda jam takimta sanctus esto ipsusit drin for the the murda insam ons indoa nurds iodsa the hrunds nursna druamet.Sanctus est Lorem sus ipsusitn theo druamet. Lorem esomzdo ipsos doloramet, deramset Das forem sus ast vero ob eosm etprsa accusam eturdn ao justo fosduno dolores etomda the jamo teclita kuasd fruda fr gubergren.</p>
  <div class="item" style="top:97px;"><span class="disc" style="background:var(--royal);">1</span><h5>SUBITLE EXAMPLE HERE</h5><p>Lorem ipsum dolor sit amet, consectetur adipiscing elit. Fusce diam tortor, mattis quis</p></div>
  <div class="item" style="top:139px;"><span class="disc" style="background:#3d5aa3;">2</span><h5>SUBITLE EXAMPLE HERE</h5><p>Lorem ipsum dolor sit amet, consectetur adipiscing elit. Fusce diam tortor, mattis quis</p></div>
  <div class="item" style="top:183px;"><span class="disc" style="background:var(--sky);">3</span><h5>SUBITLE EXAMPLE HERE</h5><p>Lorem ipsum dolor sit amet, consectetur adipiscing elit. Fusce diam tortor, mattis quis</p></div>
  <div class="photo" role="img" aria-label="Photo of a dim lab room with learners at computers"></div>
  <span class="foot-url">www.copper-lantern.com</span><span class="foot-num">11</span>
</section>

<!-- Row 7 -->
<section class="slide quiz" style="left:93px; top:1884px;">
  <h3>MINI QUIZ LAYOUT</h3>
  <p class="quiz-sub">PLEASE ANSWER THE QUESTIONS</p>
  <div class="q" style="left:36px; top:84px;"><span class="qn">1</span><span class="ql">Question</span><p>Lorem ipsum dolor sit amet, consectetur adipiscing elit. Fusce diam tortor, mattis quis dapibus</p></div>
  <div class="q" style="left:171px; top:84px;"><span class="qn">2</span><span class="ql">Question</span><p>Lorem ipsum dolor sit amet, consectetur adipiscing elit. Fusce diam tortor, mattis quis dapibus</p></div>
  <div class="q" style="left:305px; top:84px;"><span class="qn">3</span><span class="ql">Question</span><p>Lorem ipsum dolor sit amet, consectetur adipiscing elit. Fusce diam tortor, mattis quis dapibus</p></div>
  <div class="q" style="left:36px; top:136px;"><span class="qn">4</span><span class="ql">Question</span><p>Lorem ipsum dolor sit amet, consectetur adipiscing elit. Fusce diam tortor, mattis quis dapibus</p></div>
  <div class="q" style="left:171px; top:136px;"><span class="qn">5</span><span class="ql">Question</span><p>Lorem ipsum dolor sit amet, consectetur adipiscing elit. Fusce diam tortor, mattis quis dapibus</p></div>
  <div class="q" style="left:305px; top:136px;"><span class="qn">6</span><span class="ql">Question</span><p>Lorem ipsum dolor sit amet, consectetur adipiscing elit. Fusce diam tortor, mattis quis dapibus</p></div>
  <div class="q" style="left:36px; top:188px;"><span class="qn">7</span><span class="ql">Question</span><p>Lorem ipsum dolor sit amet, consectetur adipiscing elit. Fusce diam tortor, mattis quis dapibus</p></div>
  <div class="q" style="left:171px; top:188px;"><span class="qn">8</span><span class="ql">Question</span><p>Lorem ipsum dolor sit amet, consectetur adipiscing elit. Fusce diam tortor, mattis quis dapibus</p></div>
  <div class="q" style="left:305px; top:188px;"><span class="qn">9</span><span class="ql">Question</span><p>Lorem ipsum dolor sit amet, consectetur adipiscing elit. Fusce diam tortor, mattis quis dapibus</p></div>
  <span class="foot-url">www.copper-lantern.com</span>
</section>

<section class="slide point" style="left:659px; top:1884px;">
  <h3 class="slide-title">Important Point</h3><div class="rule"></div>
  <span class="mark">Copper Lantern</span>
  <p class="copy">Lorem esomzdo ipsos doloramet, deramset. Fosduom dolores etomda jam takimta sanctus esto ipsusit drin for the the murda insam ons indoa nurds iodsa the hrunds nursna druamet.Sanctus est Lorem sus ipsusitn theo druamet. Lorem esomzdo ipsos doloramet, deramset Das forem sus ast vero ob eosm etprsa accusam eturdn ao justo fosduno dolores etomda the jamo teclita kuasd fruda fr gubergren. Nosotra seada meram ontsem takimata sanctus est ses drumas vero eoaccusam ida etois. Lorem esomzdo ipsos doloramet, deramset. Fosduom dolores etomda jam takimta sanctus esto ipsusit drin for the the murda insam ons indoa nurds iodsa the hrunds nursna druamet.Sanctus est Lorem sus ipsusitn theo druamet. Lorem esomzdo ipsos doloramet, deramset Das forem sus ast vero ob eosm etprsa accusam</p>
  <div class="photo" role="img" aria-label="Photo of learners working at laptops in a training room"></div>
  <span class="foot-url">www.copper-lantern.com</span><span class="foot-num">14</span>
</section>

</body>
</html>
```